Agriculture Business Card

I want to use my existing logo and use my tagline of "Don't Guess...Soil Test" on the card. Looking for a double sided card that will really get peoples attention.
Contact Info:
Brisco Harvest Crop Solutions
Calvin Brisco
2917 K Lane
Otoe, NE 68539
402-815-2493
calvin.r.brisco@furrowpost.net

```html
<!DOCTYPE html>
<html lang="en">
<head>
<meta charset="utf-8">
<title>Brisco Harvest Crop Solutions — Business Card</title>
<link href="https://fonts.googleapis.com/css2?family=Fira+Sans+Condensed:wght@600;700&family=Yanone+Kaffeesatz:wght@500&display=swap" rel="stylesheet">
<style>
  :root {
    --backdrop: #c2c3c5;
    --card: #ffffff;
    --brown: #9a5a3a;
    --gold: #f5b21e;
    --green: #3db04a;
    --leaf: #78c043;
  }
  html, body {
    margin: 0;
    padding: 0;
    width: 900px;
    height: 1200px;
    overflow: hidden;
    background: var(--backdrop);
  }
  .card {
    position: absolute;
    width: 656px;
    height: 375px;
    left: 123px;
    background: var(--card);
    border-radius: 11px;
    overflow: hidden;
  }
  .card--front { top: 190px; }
  .card--back { top: 622px; }

  .brand-name {
    font-family: "Yanone Kaffeesatz", "Arial Narrow", sans-serif;
    font-weight: 500;
    color: var(--brown);
    text-align: center;
    line-height: 0.98;
    margin: 0;
  }
  .brand-mark {
    position: absolute;
    border-radius: 50%;
    background: var(--gold);
  }

  .card--front .brand-mark {
    width: 74px; height: 74px;
    left: 291px; top: 120px;
  }
  .card--front .brand-name {
    position: absolute;
    left: 0; right: 0; top: 232px;
    font-size: 29px;
  }

  .card--back .brand-name {
    position: absolute;
    left: 368px; width: 260px; top: 34px;
    font-size: 36px;
  }
  .card--back .brand-mark {
    width: 66px; height: 66px;
    left: 465px; top: 160px;
  }

  .contact {
    position: absolute;
    left: 53px;
    top: 92px;
    font-family: "Fira Sans Condensed", "Arial Narrow", sans-serif;
    color: var(--brown);
    font-weight: 600;
  }
  .contact__name {
    margin: 0;
    color: var(--gold);
    font-weight: 700;
    font-size: 28px;
    letter-spacing: 0.5px;
    line-height: 1;
  }
  .contact__role {
    margin: 2px 0 0;
    font-size: 15px;
    letter-spacing: 0.5px;
  }
  .contact__rule {
    width: 105px;
    height: 1px;
    background: var(--gold);
    border: 0;
    margin: 12px 0 8px;
  }
  .contact__address {
    margin: 0;
    font-size: 15px;
    line-height: 27px;
    font-style: normal;
    letter-spacing: 0.6px;
  }
  .contact__line {
    display: flex;
    align-items: center;
    gap: 7px;
    font-size: 15px;
    line-height: 25px;
    letter-spacing: 0.6px;
    margin: 0;
  }
  .contact__list { margin-top: 8px; }
  .contact__line svg { width: 13px; height: 13px; fill: var(--gold); }

  .swoosh {
    position: absolute;
    left: 0; bottom: 0;
    width: 656px; height: 60px;
  }
  .tagline {
    position: absolute;
    left: 415px;
    top: 347px;
    margin: 0;
    font-family: "Fira Sans Condensed", "Arial Narrow", sans-serif;
    font-weight: 600;
    font-size: 14px;
    letter-spacing: 1px;
    color: #ffffff;
  }
</style>
</head>
<body>

  <section class="card card--front">
    <span class="brand-mark" aria-hidden="true"></span>
    <p class="brand-name">Brisco Harvest Crop<br>Solutions</p>
  </section>

  <section class="card card--back">
    <div class="contact">
      <h1 class="contact__name">CALVIN BRISCO</h1>
      <p class="contact__role">Owner</p>
      <hr class="contact__rule">
      <address class="contact__address">2917 K Lane<br>Otoe, NE 68539</address>
      <hr class="contact__rule">
      <div class="contact__list">
        <p class="contact__line">
          <svg viewBox="0 0 24 24" aria-hidden="true"><path d="M6.6 10.8a15.1 15.1 0 0 0 6.6 6.6l2.2-2.2c.3-.3.7-.4 1-.2 1.1.4 2.3.6 3.6.6.6 0 1 .4 1 1V20c0 .6-.4 1-1 1C10.6 21 3 13.4 3 4c0-.6.4-1 1-1h3.5c.6 0 1 .4 1 1 0 1.3.2 2.5.6 3.6.1.3 0 .7-.2 1z"/></svg>
          402-815-2493
        </p>
        <p class="contact__line">
          <svg viewBox="0 0 24 24" aria-hidden="true"><path d="M2 5h20v14H2z M2 5l10 8 10-8" stroke="#fff" stroke-width="1.6"/></svg>
          calvin.r.brisco@furrowpost.net
        </p>
      </div>
    </div>

    <p class="brand-name">Brisco Harvest Crop<br>Solutions</p>
    <span class="brand-mark" aria-hidden="true"></span>

    <svg class="swoosh" viewBox="0 0 656 60" preserveAspectRatio="none" aria-hidden="true">
      <path d="M56 60 Q 250 22 480 12 L 300 16 Q 180 24 56 60 Z" fill="var(--gold)"/>
      <path d="M100 60 Q 330 18 656 10 L 656 60 Z" fill="var(--green)"/>
    </svg>
    <p class="tagline">DON'T GUESS...SOIL TEST</p>
  </section>

</body>
</html>
```